professional health club Info Flyer

we need a professional health club DL flyer that will provide information regarding our 24/7 health club services to enquiries whilst we are unstaffed. these will be placed outside on main street.

www.fitrova.club

On the reverse side, we want to offer 2 introductory specials;
1. free 7 day trial
2. Membership, classes & personal training introductory month3 personal training sessions and month 24/7 membership and classes for $99.95 (saving of over $159.85)
conditions: valid for new members only

SIZE: DL with double sided

Target Market(s)

professional, male and female of all ages (in particular those 30+)

Industry/Entity Type

Health And Wellness

Colors
33a6d7
abd037
f78f20
ffffff

Requirements
Must have
• - professional allied health feel about flyer with images
• - contact details
• - services provided include 24/7 memberships, classes, special population group training, Exercise physiology, physiotherapy, massage, nutrition, rehabilitation.
• - a catch to get them to contact us
• - our slogan "We are here to improve your quality of life"

```html
<!DOCTYPE html>
<html lang="en">
<head>
<meta charset="utf-8">
<title>Fitrova Health Club – DL Flyer</title>
<link href="https://fonts.googleapis.com/css2?family=Bebas+Neue&family=Exo+2:ital,wght@0,700;0,800;1,800&family=Lato:wght@400;700;900&display=swap" rel="stylesheet">
<style>
  :root{
    --navy:#1f4590;
    --cyan:#3cbbe6;
    --cyan-deep:#33a6d7;
    --lime:#abd037;
    --orange:#f78f20;
    --white:#ffffff;
    --grey:#dcdfe1;
    --stage:#efefef;
    --ink:#2a2a2a;
  }
  *{box-sizing:border-box;margin:0;padding:0}
  html,body{width:1200px;height:1200px;overflow:hidden}
  body{background:var(--stage);position:relative;font-family:'Lato',sans-serif;color:var(--ink)}
  .panel{position:absolute;top:53px;width:466px;height:1049px;background:var(--white);overflow:hidden;box-shadow:0 4px 14px rgba(0,0,0,.18)}
  .panel--front{left:129px}
  .panel--back{left:662px}
  .side-label{position:absolute;font-family:'Lato',sans-serif;font-size:24px;color:#111;transform:translateX(-50%)}
  .side-label--front{left:342px;top:1126px}
  .side-label--back{left:895px;top:1117px}

  .brand{position:absolute;display:flex;align-items:center;gap:12px}
  .brand__dot{width:52px;height:52px;border-radius:50%;background:var(--cyan)}
  .brand__name{font-family:'Exo 2',sans-serif;font-weight:700;font-size:48px;color:var(--navy);letter-spacing:1px;line-height:1}
  .tagline{position:absolute;font-family:'Exo 2',sans-serif;font-style:italic;font-weight:800;color:var(--navy)}

  /* front */
  .front .brand{left:108px;top:40px}
  .front .tagline{left:108px;top:114px;font-size:17px}
  .front__frame{position:absolute;left:0;top:150px;width:466px;height:620px;background:var(--cyan);border-top-left-radius:70px}
  .front__photo{position:absolute;left:10px;top:163px;width:441px;height:498px;border-radius:55px 0 60px 0;background:linear-gradient(180deg,#e8eef0 0%,#9fb4b8 35%,#51625f 65%,#2c3936 100%);border:2px solid #fff}
  .front__info{position:absolute;left:0;top:679px;width:466px;height:270px;background:linear-gradient(180deg,#e9ecee,#d2d6d9);border-top-right-radius:90px}
  .front__heading{position:absolute;left:24px;top:720px;font-family:'Exo 2',sans-serif;font-weight:800;font-size:40px;color:var(--cyan);letter-spacing:1px;line-height:1}
  .front__sub{position:absolute;left:25px;top:764px;font-family:'Exo 2',sans-serif;font-style:italic;font-weight:800;font-size:26px;color:var(--navy)}
  .services{position:absolute;top:810px;list-style:none}
  .services--left{left:25px}
  .services--right{left:269px}
  .services li{font-size:13px;color:#444;height:21px;display:flex;align-items:center;gap:10px}
  .services li::before{content:"";width:10px;height:10px;border-radius:50%;background:var(--cyan-deep);flex:none}

  /* footer shared */
  .footer-curve{position:absolute;left:0;width:466px;height:130px;background:var(--cyan);border-top-left-radius:70px}
  .footer{position:absolute;left:0;width:466px;height:120px;background:var(--navy);border-top-left-radius:66px;color:#fff}
  .contact{position:absolute;list-style:none;font-size:16px}
  .contact li{display:flex;align-items:center;gap:10px;height:23px}
  .contact li:first-child{font-weight:700}
  .contact svg{width:16px;height:16px;flex:none}
  .address{position:absolute;font-size:16px;line-height:20px;display:flex;gap:8px}
  .address svg{width:18px;height:18px;flex:none}

  .front .footer-curve{top:932px}
  .front .footer{top:942px}
  .front .contact{left:62px;top:14px}
  .front .address{left:245px;top:16px}

  /* back */
  .back__band{position:absolute;left:0;top:0;width:466px;height:30px;background:var(--navy)}
  .back .brand{left:42px;top:66px}
  .back .brand__dot{width:44px;height:44px}
  .back .brand__name{font-size:40px}
  .back .tagline{left:42px;top:124px;font-size:14px}
  .back__curve{position:absolute;left:0;top:150px;width:466px;height:488px;background:var(--cyan);border-bottom-left-radius:130px}
  .back__photo{position:absolute;left:0;top:60px;width:466px;height:570px;background:linear-gradient(160deg,#ffffff 0%,#f1f1f1 30%,#b9a89a 60%,#3b3f4d 100%);border-bottom-left-radius:125px}
  .badge{position:absolute;left:220px;top:526px;width:216px;height:216px;border-radius:50%;background:var(--navy);border:4px solid var(--white);box-shadow:0 0 0 4px var(--navy);display:flex;flex-direction:column;align-items:center;justify-content:center;font-family:'Bebas Neue',sans-serif;color:#fff;line-height:.9}
  .badge__free{font-size:66px}
  .badge__trial{font-size:50px}
  .offers__title{position:absolute;left:26px;top:740px;font-family:'Bebas Neue',sans-serif;font-size:36px;color:var(--cyan-deep);letter-spacing:.5px}
  .offer{position:absolute;left:30px;font-size:19px;line-height:23px;padding-left:22px;color:#222}
  .offer::before{content:"";position:absolute;left:0;top:5px;width:15px;height:15px;border-radius:50%;background:var(--cyan)}
  .offer b{font-weight:900}
  .offer--one{top:790px}
  .offer--two{top:857px}
  .back .footer-curve{top:928px}
  .back .footer{top:938px}
  .back .contact{left:26px;top:18px}
  .back .address{left:206px;top:18px}
</style>
</head>
<body>

<section class="panel panel--front front">
  <div class="brand"><span class="brand__dot"></span><span class="brand__name">fitrova</span></div>
  <p class="tagline">Improving your quality of life</p>
  <div class="front__frame"></div>
  <div class="front__photo" role="img" aria-label="Photo of the gym floor with weight machines and cardio equipment"></div>
  <div class="front__info"></div>
  <h1 class="front__heading">WE ARE HERE TO</h1>
  <p class="front__sub">improve your quality of life</p>
  <ul class="services services--left">
    <li>24/7 memberships</li>
    <li>Classes</li>
    <li>Special population group training</li>
    <li>Exercise physiology</li>
  </ul>
  <ul class="services services--right">
    <li>Physiotherapy</li>
    <li>Massage</li>
    <li>Nutrition</li>
    <li>Rehabilitation</li>
  </ul>
  <div class="footer-curve"></div>
  <footer class="footer">
    <ul class="contact">
      <li><svg viewBox="0 0 16 16"><rect x="1" y="3" width="14" height="11" rx="2" fill="none" stroke="#fff" stroke-width="1.4"/><rect x="4" y="6" width="8" height="2" fill="#fff"/></svg>+612 85550192</li>
      <li><svg viewBox="0 0 16 16"><rect x="1" y="3" width="14" height="10" fill="none" stroke="#fff" stroke-width="1.4"/><path d="M1 3l7 6 7-6" fill="none" stroke="#fff" stroke-width="1.4"/></svg>jordan@fitrova.club</li>
      <li><svg viewBox="0 0 16 16"><circle cx="8" cy="8" r="6.5" fill="none" stroke="#fff" stroke-width="1.4"/><path d="M1.5 8h13M8 1.5c-3 3.5-3 9.5 0 13M8 1.5c3 3.5 3 9.5 0 13" fill="none" stroke="#fff" stroke-width="1.2"/></svg>www.fitrova.club</li>
    </ul>
    <div class="address">
      <svg viewBox="0 0 18 18"><path d="M2 9L9 2l7 7M4 8v8h4v-5h2v5h4V8" fill="none" stroke="#fff" stroke-width="1.6"/></svg>
      <p>58 Kingsway Parade<br>Marlowe Bay Sydney<br>NSW 2231</p>
    </div>
  </footer>
</section>

<section class="panel panel--back back">
  <div class="back__band"></div>
  <div class="back__curve"></div>
  <div class="back__photo" role="img" aria-label="Photo of four smiling gym members in workout clothes beside dumbbells"></div>
  <div class="brand"><span class="brand__dot"></span><span class="brand__name">fitrova</span></div>
  <p class="tagline">Improving your quality of life</p>
  <div class="badge"><span class="badge__free">FREE</span><span class="badge__trial">7 DAY TRIAL</span></div>
  <h2 class="offers__title">MEMBERSHIP &amp; CLASSES</h2>
  <p class="offer offer--one">Personal training introductory<br><b>month 3 personal training sessions</b></p>
  <p class="offer offer--two">Month <b>24/7</b> membership and classes<br>for <b>$99.95</b> (saving of over <b>$159.85</b>)</p>
  <div class="footer-curve"></div>
  <footer class="footer">
    <ul class="contact">
      <li><svg viewBox="0 0 16 16"><rect x="1" y="3" width="14" height="11" rx="2" fill="none" stroke="#fff" stroke-width="1.4"/><rect x="4" y="6" width="8" height="2" fill="#fff"/></svg>+612 85550192</li>
      <li><svg viewBox="0 0 16 16"><rect x="1" y="3" width="14" height="10" fill="none" stroke="#fff" stroke-width="1.4"/><path d="M1 3l7 6 7-6" fill="none" stroke="#fff" stroke-width="1.4"/></svg>jordan@fitrova.club</li>
      <li><svg viewBox="0 0 16 16"><circle cx="8" cy="8" r="6.5" fill="none" stroke="#fff" stroke-width="1.4"/><path d="M1.5 8h13M8 1.5c-3 3.5-3 9.5 0 13M8 1.5c3 3.5 3 9.5 0 13" fill="none" stroke="#fff" stroke-width="1.2"/></svg>www.fitrova.club</li>
    </ul>
    <div class="address">
      <svg viewBox="0 0 18 18"><path d="M2 9L9 2l7 7M4 8v8h4v-5h2v5h4V8" fill="none" stroke="#fff" stroke-width="1.6"/></svg>
      <p>58 Kingsway Parade<br>Marlowe Bay Sydney<br>NSW 2231</p>
    </div>
  </footer>
</section>

<p class="side-label side-label--front">FRONT</p>
<p class="side-label side-label--back">BACK</p>

</body>
</html>
```